Step Up Personal Training Sessions

Whether you have a lot to give out or a little...just Step Up. Whether you are strong or you desire to get there... just Step Up. Stay Bold Feel Free. PT's with a passionate coach.

I had imagined black and white or indigo/white. Communicate love, people and fitness.

Target Market(s)

Women, men, disabilities. People whom wish to move more, or who do not desire to go to a gym. One on one fitness or small group training.

Industry/Entity Type

Training

Contact Information for Business Card

Kim Farrow
0431 592 604
kimjoanne@wavenet.example

Font styles to use
Decorative

Colors
0d0d0d
1b1b1b

Requirements
Must have
• Step Up
• Personal Fitness Sessions
• Stay Bold Feel Free
• ( my details above )
Nice to have
• If any part of the project description ....Whether....etc
• can be fit onto card. That would be great. I had ideas of Heart, people exercising, I love boxing training, so this idea was in my head, not sure how to bring all together. Would also like to work with disabilities.
Should not have
• Cannot think of any not haves at this stage.
• Colours at the bottom of page, either green is ok, with charcoal or navy. Not both these colours together.

```html
<!DOCTYPE html>
<html lang="en">
<head>
<meta charset="utf-8">
<title>Step Up Personal Training – Business Card Options</title>
<link rel="stylesheet" href="https://fonts.googleapis.com/css2?family=Exo+2:wght@700;800&family=Signika:wght@300;400;700&display=swap">
<style>
  :root {
    --page-bg: #9a9a9a;
    --label: #ffffff;
    --white: #ffffff;
    --charcoal: #424242;
    --charcoal-band: #3a3a3a;
    --red: #e31e24;
    --navy: #22325f;
    --navy-band: #233262;
    --slate: #7a7a88;
    --green: #2a9b4a;
    --mint: #5fbf8c;
    --figure-light: #f2f2f2;
    --figure-lilac: #b8bcd8;
  }
  * { box-sizing: border-box; margin: 0; padding: 0; }
  html, body { width: 1135px; height: 1200px; overflow: hidden; }
  body { background: var(--page-bg); position: relative; font-family: "Signika", sans-serif; }

  .option-label {
    position: absolute; left: 72px;
    font: 700 34px "Signika", sans-serif; color: var(--label);
  }

  .card {
    --accent: var(--red);
    --sweep-left: var(--charcoal);
    --ink: var(--charcoal);
    --icon: var(--red);
    --band: var(--charcoal-band);
    --divider: var(--red);
    --bullet: var(--red);
    --figures: var(--figure-light);
    position: absolute; width: 781px; height: 469px;
    background: var(--white);
    box-shadow: 0 3px 8px rgba(0,0,0,.3);
    overflow: hidden;
  }
  .card--navy {
    --accent: var(--navy);
    --sweep-left: var(--slate);
    --ink: var(--navy);
    --icon: var(--mint);
    --band: var(--navy-band);
    --divider: var(--slate);
    --bullet: var(--green);
    --figures: var(--figure-lilac);
  }
  .card--charcoal { left: 191px; top: 92px; }
  .card--navy { left: 193px; top: 644px; }

  .card__sweep { position: absolute; left: 0; top: 0; width: 781px; height: 110px; }
  .card__sweep .sweep-left { fill: var(--sweep-left); }
  .card__sweep .sweep-right { fill: var(--accent); }

  .brand-mark {
    position: absolute; left: 80px; top: 100px; width: 190px; height: 80px;
    display: flex; align-items: center; justify-content: center;
    font: 800 38px "Exo 2", sans-serif; color: var(--accent);
  }

  .contact { position: absolute; left: 346px; top: 62px; color: var(--ink); }
  .contact__name { font: 700 29px "Signika", sans-serif; color: var(--ink); letter-spacing: .5px; }
  .contact__tagline { font: 300 21px "Signika", sans-serif; color: var(--charcoal); margin-top: 6px; }
  .card--navy .contact__tagline { color: var(--navy); }
  .contact__line {
    display: flex; align-items: center; gap: 14px;
    font: 300 25px "Signika", sans-serif; color: var(--charcoal); margin-top: 12px;
  }
  .card--navy .contact__line { color: var(--navy); }
  .contact__line svg { width: 26px; height: 30px; flex: none; }
  .contact__line svg .icon-stroke { fill: none; stroke: var(--icon); stroke-width: 2.6; }
  .contact__line svg .icon-fill { fill: var(--icon); }

  .card__divider { position: absolute; left: 0; top: 243px; width: 100%; height: 6px; background: var(--divider); }
  .card__band { position: absolute; left: 0; top: 249px; width: 100%; height: 220px; background: var(--band); }

  .services { position: absolute; left: 53px; top: 52px; list-style: none; }
  .services li {
    position: relative; padding-left: 22px;
    font: 700 24px "Exo 2", sans-serif; color: var(--white); line-height: 32px;
  }
  .services li::before {
    content: ""; position: absolute; left: 0; top: 11px;
    width: 11px; height: 11px; border-radius: 50%; background: var(--bullet);
  }

  .exercise-figures {
    position: absolute; left: 400px; top: 4px; width: 345px; height: 204px;
    border-radius: 8px; background: var(--figures); opacity: .22;
  }
</style>
</head>
<body>

<div class="option-label" style="top:325px">1</div>
<div class="option-label" style="top:848px">2</div>

<article class="card card--charcoal">
  <svg class="card__sweep" viewBox="0 0 781 110" aria-hidden="true">
    <path class="sweep-left" d="M0 0 H520 Q230 14 0 80 Z"/>
    <path class="sweep-right" d="M300 0 H781 V76 Q560 10 300 0 Z"/>
  </svg>
  <div class="brand-mark">Step Up</div>
  <div class="contact">
    <div class="contact__name">Kim Farrow</div>
    <div class="contact__tagline">PT's with a passionate coach</div>
    <div class="contact__line">
      <svg viewBox="0 0 26 30" aria-hidden="true"><rect class="icon-stroke" x="5" y="2" width="16" height="26" rx="2"/><line class="icon-stroke" x1="10" y1="24" x2="16" y2="24"/></svg>
      0431 592 604
    </div>
    <div class="contact__line">
      <svg viewBox="0 0 26 30" aria-hidden="true"><path class="icon-fill" d="M1 12 L13 5 L25 12 V25 H1 Z"/><path d="M1 12 L13 20 L25 12" fill="none" stroke="#fff" stroke-width="1.6"/></svg>
      kimjoanne@wavenet.example
    </div>
  </div>
  <div class="card__divider"></div>
  <div class="card__band">
    <ul class="services">
      <li>Step Up</li>
      <li>Personal Fitness Sessions</li>
      <li>Stay Bold Feel Free</li>
    </ul>
    <div class="exercise-figures" role="img" aria-label="Silhouettes of people exercising: stretching, sit-ups, stepping, running, boxing, lunging, flexing and martial arts"></div>
  </div>
</article>

<article class="card card--navy">
  <svg class="card__sweep" viewBox="0 0 781 110" aria-hidden="true">
    <path class="sweep-left" d="M0 0 H520 Q230 14 0 80 Z"/>
    <path class="sweep-right" d="M300 0 H781 V76 Q560 10 300 0 Z"/>
  </svg>
  <div class="brand-mark">Step Up</div>
  <div class="contact">
    <div class="contact__name">Kim Farrow</div>
    <div class="contact__tagline">PT's with a passionate coach</div>
    <div class="contact__line">
      <svg viewBox="0 0 26 30" aria-hidden="true"><rect class="icon-stroke" x="5" y="2" width="16" height="26" rx="2"/><line class="icon-stroke" x1="10" y1="24" x2="16" y2="24"/></svg>
      0431 592 604
    </div>
    <div class="contact__line">
      <svg viewBox="0 0 26 30" aria-hidden="true"><path class="icon-fill" d="M1 12 L13 5 L25 12 V25 H1 Z"/><path d="M1 12 L13 20 L25 12" fill="none" stroke="#fff" stroke-width="1.6"/></svg>
      kimjoanne@wavenet.example
    </div>
  </div>
  <div class="card__divider"></div>
  <div class="card__band">
    <ul class="services">
      <li>Step Up</li>
      <li>Personal Fitness Sessions</li>
      <li>Stay Bold Feel Free</li>
    </ul>
    <div class="exercise-figures" role="img" aria-label="Silhouettes of people exercising: stretching, sit-ups, stepping, running, boxing, lunging, flexing and martial arts"></div>
  </div>
</article>

</body>
</html>
```